Product flyer with pricing

We manufacture iconic and luxury vending trailers. for our first trailer we need a flyer created to give to prospective clients with base pricing. I am uploading an example along with graphic files.

```html
<!DOCTYPE html>
<html lang="en">
<head>
<meta charset="utf-8">
<title>Meadow Cottage Mini – Vending House Flyer</title>
<link href="https://fonts.googleapis.com/css2?family=Montserrat:wght@500;600;700;800&family=Oswald:wght@400;500&family=Open+Sans:wght@400;600&display=swap" rel="stylesheet">
<style>
  :root{
    --orange:#e9a42a;
    --green:#5ea63b;
    --ink:#2f2f2f;
    --muted:#4a4a4a;
    --header-dark:#55585a;
    --header-light:#7b7e80;
    --paper:#ffffff;
    --stage:#f2f2f2;
  }
  *{box-sizing:border-box;margin:0;padding:0}
  html,body{width:839px;height:1200px;overflow:hidden;background:var(--stage)}
  .flyer{position:relative;width:839px;height:1200px;background:var(--paper);font-family:"Open Sans",Arial,sans-serif;color:var(--ink);overflow:hidden}

  .hero{position:absolute;left:0;top:0;width:839px;height:400px;
    background:linear-gradient(180deg,var(--header-light) 0%,var(--header-dark) 55%,#4b4d4f 100%)}
  .hero-stripe{position:absolute;left:0;top:400px;width:839px;height:6px;background:var(--green)}
  .brand-arc{position:absolute;left:232px;top:-150px;width:375px;height:300px;border-radius:50%;background:var(--paper);
    display:flex;align-items:flex-end;justify-content:center;padding-bottom:38px}
  .brand-name{font-family:"Montserrat",sans-serif;font-weight:800;font-size:24px;color:var(--green);display:flex;align-items:center;gap:8px;letter-spacing:.5px}
  .brand-name .dot{width:14px;height:14px;border-radius:50%;background:var(--orange)}

  .title{position:absolute;left:0;top:188px;width:839px;text-align:center;font-family:"Montserrat",sans-serif;font-weight:800;line-height:1}
  .title .the{font-size:56px;color:#fff}
  .title .model{font-size:47px;color:var(--orange);margin-top:10px;letter-spacing:1px}
  .title .tagline{font-size:38px;color:#fff;margin-top:10px;font-weight:700;letter-spacing:1px}
  .title .tagline span{color:var(--orange)}

  .section-title{font-family:"Montserrat",sans-serif;font-weight:700;font-size:24px;color:var(--ink)}
  .section-title span{color:var(--orange)}
  .section-title::after{content:"";display:block;width:52px;height:4px;background:var(--green);margin-top:9px}

  .features{position:absolute;left:28px;top:432px;width:560px}
  .features-head{display:flex;align-items:flex-start;gap:22px}
  .price-pill{display:flex;align-items:center;border:2px dashed var(--orange);border-radius:12px;height:44px;margin-top:-4px}
  .price-pill .label{background:var(--orange);color:#fff;font-family:"Montserrat",sans-serif;font-weight:600;font-size:20px;height:44px;line-height:44px;padding:0 10px;border-radius:10px}
  .price-pill .value{font-family:"Oswald",sans-serif;font-size:30px;color:var(--green);padding:0 10px}
  sup{font-size:.5em;vertical-align:top;position:relative;top:.15em}

  .checklist{display:grid;grid-template-columns:320px 220px;column-gap:20px;margin-top:18px}
  .checklist ul{list-style:none}
  .checklist li{position:relative;padding-left:22px;font-size:11.5px;line-height:1.3;margin-bottom:10px;color:var(--muted)}
  .checklist li svg{position:absolute;left:0;top:2px}

  .gallery{position:absolute;left:623px;top:428px;width:190px;display:grid;grid-template-columns:1fr 1fr;gap:12px}
  .gallery .shot{height:106px;border:3px solid var(--orange);border-radius:8px;background:linear-gradient(160deg,#9ec3e6 0%,#d9dde0 48%,#f4f4f4 60%,#5b5d5e 100%)}

  .options{position:absolute;left:28px;top:680px;width:783px}
  .option-row{display:flex;gap:20px;margin-top:22px}
  .option{border:2px solid var(--orange);border-radius:8px;overflow:hidden;text-align:center;background:#fff}
  .option .tag{background:var(--orange);color:#fff;font-family:"Montserrat",sans-serif;font-weight:600;font-size:11px;line-height:1.15;height:36px;display:flex;align-items:center;justify-content:center;padding:0 8px}
  .option .cost{font-family:"Oswald",sans-serif;font-size:33px;color:var(--green);height:50px;line-height:50px}
  .option .cost.range{font-size:24px}
  .note{font-family:"Montserrat",sans-serif;font-weight:500;font-size:15px;margin-top:14px}

  .uses{position:absolute;left:28px;top:905px;width:783px}
  .use-row{display:flex;margin-top:22px}
  .use{flex:1;text-align:center;padding:0 8px;border-right:1.5px dashed #9a9a9a}
  .use:last-child{border-right:none}
  .use svg{display:block;margin:0 auto 6px}
  .use h3{font-family:"Montserrat",sans-serif;font-weight:700;font-size:16px;color:var(--ink)}
  .use p{font-size:11px;line-height:1.35;color:var(--muted);margin-top:4px}

  .footer{position:absolute;left:0;top:1118px;width:839px;height:82px}
  .footer svg.band{position:absolute;inset:0}
  .phone{position:absolute;left:26px;top:0;height:82px;display:flex;align-items:center;gap:10px;font-family:"Montserrat",sans-serif;font-weight:600;font-size:29px;color:#fff}
  .contact{position:absolute;left:330px;top:0;height:82px;display:flex;align-items:center;gap:26px;font-size:14px;color:#fff}
  .contact span{display:flex;align-items:center;gap:7px}
</style>
</head>
<body>
<main class="flyer">
  <header>
    <div class="hero" role="img" aria-label="Photo of the white vending cottage trailer with dark roof, under a grey overlay"></div>
    <div class="hero-stripe"></div>
    <div class="brand-arc"><div class="brand-name"><i class="dot"></i>SUNROOT CABINS</div></div>
    <div class="title">
      <div class="the">THE</div>
      <div class="model">“MEADOW COTTAGE MINI”</div>
      <div class="tagline">LUXURY, MOBILE <span>VENDING HOUSE</span></div>
    </div>
  </header>

  <section class="features">
    <div class="features-head">
      <h2 class="section-title">Base unit <span>features:</span></h2>
      <div class="price-pill"><span class="label">Base price:</span><span class="value"><sup>$</sup>45,000</span></div>
    </div>
    <div class="checklist">
      <ul>
        <li><svg width="12" height="12" viewBox="0 0 12 12"><rect x=".75" y=".75" width="10.5" height="10.5" fill="none" stroke="#5ea63b" stroke-width="1.2"/><path d="M3 6l2 2 4-5" fill="none" stroke="#5ea63b" stroke-width="1.4"/></svg>Trailer features tandem wheels w/ brakes</li>
        <li><svg width="12" height="12" viewBox="0 0 12 12"><rect x=".75" y=".75" width="10.5" height="10.5" fill="none" stroke="#5ea63b" stroke-width="1.2"/><path d="M3 6l2 2 4-5" fill="none" stroke="#5ea63b" stroke-width="1.4"/></svg>Steel frame construction for fire retardation safety and weight reduction.</li>
        <li><svg width="12" height="12" viewBox="0 0 12 12"><rect x=".75" y=".75" width="10.5" height="10.5" fill="none" stroke="#5ea63b" stroke-width="1.2"/><path d="M3 6l2 2 4-5" fill="none" stroke="#5ea63b" stroke-width="1.4"/></svg>100% off grid with solar and lithium battery system allowing the trailer to be used in places not accessible by traditional trailers.</li>
      </ul>
      <ul>
        <li><svg width="12" height="12" viewBox="0 0 12 12"><rect x=".75" y=".75" width="10.5" height="10.5" fill="none" stroke="#5ea63b" stroke-width="1.2"/><path d="M3 6l2 2 4-5" fill="none" stroke="#5ea63b" stroke-width="1.4"/></svg>80 gallon water supply tank</li>
        <li><svg width="12" height="12" viewBox="0 0 12 12"><rect x=".75" y=".75" width="10.5" height="10.5" fill="none" stroke="#5ea63b" stroke-width="1.2"/><path d="M3 6l2 2 4-5" fill="none" stroke="#5ea63b" stroke-width="1.4"/></svg>100 gallon waste water tank</li>
        <li><svg width="12" height="12" viewBox="0 0 12 12"><rect x=".75" y=".75" width="10.5" height="10.5" fill="none" stroke="#5ea63b" stroke-width="1.2"/><path d="M3 6l2 2 4-5" fill="none" stroke="#5ea63b" stroke-width="1.4"/></svg>Cupboards, cabinets &amp; four stainless steel sinks.</li>
        <li><svg width="12" height="12" viewBox="0 0 12 12"><rect x=".75" y=".75" width="10.5" height="10.5" fill="none" stroke="#5ea63b" stroke-width="1.2"/><path d="M3 6l2 2 4-5" fill="none" stroke="#5ea63b" stroke-width="1.4"/></svg>60” Gas shock serving window</li>
      </ul>
    </div>
  </section>

  <div class="gallery">
    <div class="shot" role="img" aria-label="Front view of the vending cottage with its door"></div>
    <div class="shot" role="img" aria-label="Side view with open serving window"></div>
    <div class="shot" role="img" aria-label="Side view of the trailer on tandem wheels"></div>
    <div class="shot" role="img" aria-label="Rear corner view of the trailer"></div>
  </div>

  <section class="options">
    <h2 class="section-title">Available <span>options:</span></h2>
    <div class="option-row">
      <div class="option" style="width:120px"><div class="tag">HVAC - Kelvo<br>Mini Split</div><div class="cost"><sup>$</sup>1,800</div></div>
      <div class="option" style="width:164px"><div class="tag">Cooler / Glass front<br>Commercial refrigerator</div><div class="cost"><sup>$</sup>1,600</div></div>
      <div class="option" style="width:122px"><div class="tag">Upper loft<br>storage area</div><div class="cost"><sup>$</sup>1,200</div></div>
      <div class="option" style="width:157px"><div class="tag">Signage and graphics<br>depend on complexity</div><div class="cost range"><sup>$</sup>2,000 - <sup>$</sup>5,000</div></div>
      <div class="option" style="width:120px"><div class="tag">Ice machine</div><div class="cost"><sup>$</sup>1,100</div></div>
    </div>
    <p class="note">Other custom items available on request.</p>
  </section>

  <section class="uses">
    <h2 class="section-title">Use <span>cases:</span></h2>
    <div class="use-row">
      <div class="use">
        <svg width="30" height="30" viewBox="0 0 30 30"><circle cx="15" cy="15" r="13" fill="none" stroke="#5ea63b" stroke-width="2"/><path d="M9 18h12M10 18a5 5 0 0 1 10 0M15 11v2" fill="none" stroke="#5ea63b" stroke-width="1.8"/></svg>
        <h3>Food</h3><p>Lemonade, Coffee, pizza,<br>cookies, doughnuts,<br>barbecue and more!</p>
      </div>
      <div class="use">
        <svg width="30" height="30" viewBox="0 0 30 30"><circle cx="15" cy="15" r="13" fill="none" stroke="#5ea63b" stroke-width="2"/><path d="M8 10h2l2 8h8l2-6H11" fill="none" stroke="#5ea63b" stroke-width="1.8"/><circle cx="13" cy="21" r="1.2" fill="#5ea63b"/><circle cx="19" cy="21" r="1.2" fill="#5ea63b"/></svg>
        <h3>Retail</h3><p>Clothing, watches, jewelry,<br>flowers and more!</p>
      </div>
      <div class="use">
        <svg width="30" height="30" viewBox="0 0 30 30"><circle cx="15" cy="15" r="13" fill="none" stroke="#5ea63b" stroke-width="2"/><rect x="10" y="9" width="10" height="13" fill="none" stroke="#5ea63b" stroke-width="1.8"/><path d="M13 12h4M13 15h4M13 18h4" stroke="#5ea63b" stroke-width="1.5"/></svg>
        <h3>Corporate</h3><p>Product info, demonstration,<br>information, brand awareness.</p>
      </div>
      <div class="use">
        <svg width="30" height="30" viewBox="0 0 30 30"><circle cx="15" cy="15" r="13" fill="none" stroke="#5ea63b" stroke-width="2"/><circle cx="11" cy="12" r="2.2" fill="none" stroke="#5ea63b" stroke-width="1.6"/><circle cx="19" cy="12" r="2.2" fill="none" stroke="#5ea63b" stroke-width="1.6"/><path d="M7 21a4 4 0 0 1 8 0M15 21a4 4 0 0 1 8 0" fill="none" stroke="#5ea63b" stroke-width="1.6"/></svg>
        <h3>Fundraisers</h3><p>Girls/boy sports, non profits, etc.</p>
      </div>
    </div>
  </section>

  <footer class="footer">
    <svg class="band" width="839" height="82" viewBox="0 0 839 82"><rect width="839" height="82" fill="#e9a42a"/><polygon points="0,0 302,0 282,82 0,82" fill="#5ea63b"/><polygon points="302,0 312,0 292,82 282,82" fill="#fff"/></svg>
    <div class="phone"><svg width="24" height="24" viewBox="0 0 24 24"><path d="M6 3l3 1 1 5-2 1.5a11 11 0 0 0 5.5 5.5L15 14l5 1 1 3-2 3C10 20 4 14 3 5z" fill="none" stroke="#fff" stroke-width="2"/></svg>555-010-7788</div>
    <div class="contact">
      <span><svg width="13" height="13" viewBox="0 0 14 14"><circle cx="7" cy="7" r="6" fill="none" stroke="#fff" stroke-width="1.3"/><path d="M1 7h12M7 1c-3 3-3 9 0 12M7 1c3 3 3 9 0 12" fill="none" stroke="#fff" stroke-width="1"/></svg>www.sunrootcabins.com</span>
      <span><svg width="13" height="10" viewBox="0 0 14 10"><rect x=".5" y=".5" width="13" height="9" fill="#fff"/><path d="M.5 .5L7 6l6.5-5.5" fill="none" stroke="#e9a42a" stroke-width="1.2"/></svg>hello@sunrootcabins.com</span>
    </div>
  </footer>
</main>
</body>
</html>
```